Creative Podcast Cover Art for The Bright Harbor Venture show

We need Podcast Cover Art for our new podcast, The Bright Harbor Venture. We're looking for a clean, eye catching design that draws attention and creates curiosity. The BHV is about self improvement and creating your ideal lifestyle. We like the colors Yellow, Orange or Navy Blue and grey or white background but of course, we're open to your creativity :)

Target Market(s)

Self Improvement, Entrepreneurs

Font styles to use
Sans Serif

Requirements
Must have
• Clean font that embodies Efficiency and Optimization. I'd like to somehow incorporate a visual that reflects this is a project and something we're always working and improving on. Must grab attention and evoke curiosity.
Nice to have
• Creative artwork that reflects the concept.
Should not have
• Self Portrait.

```html
<!DOCTYPE html>
<html lang="en">
<head>
<meta charset="utf-8">
<title>The Bright Harbor Venture — Podcast Cover</title>
<link rel="stylesheet" href="https://fonts.googleapis.com/css2?family=Poppins:wght@300;600;700&display=swap">
<style>
  :root {
    --ink: #000000;
    --sky-light: #0a96f5;
    --sky-mid: #0b7fe8;
    --sky-deep: #0a5fd6;
    --title-white: #ffffff;
    --title-ice: #dfeefc;
    --brand-blue: #1570e3;
    --brand-blue-deep: #0f5fd8;
    --subtitle: #ffffff;
  }
  html, body {
    margin: 0;
    padding: 0;
    width: 1200px;
    height: 1200px;
    overflow: hidden;
    background: var(--ink);
  }
  .cover {
    position: relative;
    width: 1200px;
    height: 1200px;
    background: var(--ink);
    overflow: hidden;
  }
  .cover-art {
    position: absolute;
    inset: 0;
    width: 1200px;
    height: 1200px;
    display: block;
  }
  .title-the,
  .title-bright {
    font-family: "Poppins", sans-serif;
    font-weight: 700;
    fill: url(#titleWhite);
  }
  .title-harbor {
    font-family: "Poppins", sans-serif;
    font-weight: 700;
    fill: url(#titleBlue);
  }
  .title-venture {
    font-family: "Poppins", sans-serif;
    font-weight: 600;
    fill: url(#titleBlue);
  }
  .host-line {
    font-family: "Poppins", sans-serif;
    font-weight: 300;
    fill: var(--subtitle);
  }
  .host-bar {
    fill: var(--brand-blue);
  }
</style>
</head>
<body>
  <main class="cover">
    <svg class="cover-art" viewBox="0 0 1200 1200" xmlns="http://www.w3.org/2000/svg">
      <defs>
        <radialGradient id="heroGlow" cx="1000" cy="250" r="820" gradientUnits="userSpaceOnUse">
          <stop offset="0" stop-color="var(--sky-light)"/>
          <stop offset="0.35" stop-color="var(--sky-mid)"/>
          <stop offset="0.65" stop-color="var(--sky-deep)" stop-opacity="0.55"/>
          <stop offset="1" stop-color="var(--ink)" stop-opacity="0"/>
        </radialGradient>
        <linearGradient id="titleWhite" x1="0" y1="0" x2="1" y2="0">
          <stop offset="0" stop-color="var(--title-white)"/>
          <stop offset="1" stop-color="var(--title-ice)"/>
        </linearGradient>
        <linearGradient id="titleBlue" x1="0" y1="0" x2="1" y2="0">
          <stop offset="0" stop-color="var(--brand-blue)"/>
          <stop offset="1" stop-color="var(--brand-blue-deep)"/>
        </linearGradient>
      </defs>

      <rect class="hero-illustration" x="0" y="0" width="1200" height="1200" fill="url(#heroGlow)"
            role="img" aria-label="Illustration area: a climber silhouette pushing a large boulder up a dark hill against a cloudy blue sky"/>

      <g class="show-title">
        <text class="title-the" x="60" y="538" font-size="71">The</text>
        <text class="title-bright" x="57" y="686" font-size="140" letter-spacing="-2">BRIGHT</text>
        <text class="title-harbor" x="57" y="857" font-size="167" letter-spacing="-2">HARBOR</text>
        <text class="title-venture" x="57" y="981" font-size="126" letter-spacing="-2">Venture</text>
      </g>

      <g class="host-credit">
        <rect class="host-bar" x="62" y="1060" width="9" height="35"/>
        <text class="host-line" x="92" y="1092" font-size="35">Podcast hosted by Sam Rowley</text>
      </g>
    </svg>
  </main>
</body>
</html>
```